Marisol business card and stationary
business card and stationary
Marisol business card and stationary - Retailers
Creative Brief
Bright & Fun-filled
Janet Wroblenko
owner, designer
marisol a florist 418 north brook lane greenville, sc 29174
info@marisolblooms.example
marisolblooms.example
Concepts
Stationery for Online Retailer

```html
<!DOCTYPE html>
<html lang="en">
<head>
<meta charset="utf-8">
<title>Marisol Stationery</title>
<link href="https://fonts.googleapis.com/css2?family=Quicksand:wght@400;600&display=swap" rel="stylesheet">
<style>
:root{
  --bg:#ecebe8;
  --paper:#ffffff;
  --pink:#c9365f;
  --pink-soft:#f6d9e1;
  --green:#8fae3b;
  --ink:#6b5a5f;
  --shadow:0 10px 28px rgba(60,40,45,.18);
}
*{margin:0;padding:0;box-sizing:border-box}
html,body{width:1200px;height:1011px;overflow:hidden;background:var(--bg);font-family:"Quicksand",sans-serif;color:var(--ink)}
.canvas{position:relative;width:1200px;height:1011px}
.sheet{position:absolute;background:var(--paper);box-shadow:var(--shadow);overflow:hidden}
.corner{position:absolute}
.logo{display:flex;flex-direction:column;align-items:center;gap:6px}
.logo-flower{border-radius:50%;background:radial-gradient(circle,#f3b9c6 0%,#e07b94 60%,#d65c7d 100%)}
.logo-name{font-weight:600;color:var(--pink);letter-spacing:.5px;line-height:1}
.letterhead{left:60px;top:70px;width:560px;height:792px;background:linear-gradient(180deg,#fff 0%,#fff 78%,#fbe7ec 100%)}
.letterhead .logo{position:absolute;left:50%;top:70px;transform:translateX(-50%)}
.letterhead .logo-flower{width:90px;height:90px}
.letterhead .logo-name{font-size:30px}
.letterhead .watermark{position:absolute;left:150px;top:280px;width:260px;height:260px;border-radius:50%;background:radial-gradient(circle,rgba(230,150,170,.10),rgba(230,150,170,0) 70%)}
.letterhead .footer{position:absolute;left:40px;right:40px;bottom:26px;font-size:9px;text-align:center;letter-spacing:.3px}
.envelope{left:670px;top:70px;width:470px;height:300px;background:linear-gradient(180deg,#fff 0%,#fff 70%,#fbe4ea 100%)}
.envelope .logo{position:absolute;left:120px;top:26px}
.envelope .logo-flower{width:70px;height:70px}
.envelope .logo-name{font-size:24px}
.envelope .mini-flower{position:absolute;right:30px;top:24px;width:44px;height:44px}
.envelope .address{position:absolute;left:40px;bottom:60px;font-size:12px;letter-spacing:.4px}
.card{width:300px;height:172px}
.card-front{left:670px;top:420px;background:var(--pink)}
.card-front .logo{position:absolute;inset:0;justify-content:center}
.card-front .logo-flower{width:62px;height:62px;background:radial-gradient(circle,#fbe0e7,#f0a9ba)}
.card-front .logo-name{font-size:24px;color:#fff}
.card-back{left:840px;top:640px}
.card-back .logo{position:absolute;left:34px;top:26px}
.card-back .logo-flower{width:54px;height:54px}
.card-back .logo-name{font-size:20px}
.card-back .contact{position:absolute;left:22px;bottom:22px;font-size:7.5px;line-height:1.5}
.card-back .person{position:absolute;right:20px;top:74px;text-align:right}
.card-back .person-name{font-size:11px;font-weight:600;color:var(--pink)}
.card-back .person-role{font-size:8px}
.card-back .details{position:absolute;right:20px;top:104px;text-align:right;font-size:7.5px;line-height:1.5}
</style>
</head>
<body>
<main class="canvas">

  <section class="sheet letterhead" aria-label="Letterhead">
    <svg class="corner" style="right:0;top:0" width="300" height="90" viewBox="0 0 300 90">
      <path d="M0 0 H300 V90 C220 30 120 8 0 0Z" fill="var(--pink)"/>
      <path d="M0 4 C120 12 220 36 300 96" fill="none" stroke="var(--green)" stroke-width="3"/>
    </svg>
    <div class="watermark" role="img" aria-label="Faint flower decoration"></div>
    <div class="logo">
      <div class="logo-flower" role="img" aria-label="Flower illustration"></div>
      <span class="logo-name">marisol</span>
    </div>
    <p class="footer">marisol a florist, 418 north brook lane, greenville, sc 29174 &nbsp;|&nbsp; t: 864.555.0142 &nbsp;|&nbsp; info@marisolblooms.example &nbsp;|&nbsp; marisolblooms.example</p>
  </section>

  <section class="sheet envelope" aria-label="Envelope">
    <svg class="corner" style="left:0;top:0" width="120" height="120" viewBox="0 0 120 120">
      <path d="M0 0 H120 C60 20 20 60 0 120Z" fill="var(--pink)"/>
      <path d="M124 4 C62 24 22 64 4 124" fill="none" stroke="var(--green)" stroke-width="3"/>
    </svg>
    <div class="logo-flower mini-flower" role="img" aria-label="Small flower illustration"></div>
    <div class="logo">
      <div class="logo-flower" role="img" aria-label="Flower illustration"></div>
      <span class="logo-name">marisol</span>
    </div>
    <p class="address">marisol a florist, 418 north brook lane, greenville, sc 29174</p>
  </section>

  <section class="sheet card card-front" aria-label="Business card front">
    <div class="logo">
      <div class="logo-flower" role="img" aria-label="Flower illustration"></div>
      <span class="logo-name">marisol</span>
    </div>
  </section>

  <section class="sheet card card-back" aria-label="Business card back">
    <svg class="corner" style="left:0;bottom:0" width="90" height="90" viewBox="0 0 90 90">
      <path d="M0 90 V0 C18 40 48 72 90 90Z" fill="var(--pink)"/>
      <path d="M-4 0 C14 42 46 76 92 94" fill="none" stroke="var(--green)" stroke-width="2"/>
    </svg>
    <div class="logo">
      <div class="logo-flower" role="img" aria-label="Flower illustration"></div>
      <span class="logo-name">marisol</span>
    </div>
    <div class="person">
      <p class="person-name">Janet Wroblenko</p>
      <p class="person-role">owner, designer</p>
    </div>
    <div class="details">
      <p>t: 864.555.0142</p>
      <p>info@marisolblooms.example</p>
      <p>marisolblooms.example</p>
    </div>
    <div class="contact" style="left:100px">
      <p>marisol a florist</p>
      <p>418 north brook lane, greenville, sc 29174</p>
    </div>
  </section>

</main>
</body>
</html>
```